Packaging Artwork for "Earth's First Expanding Biodisposable Loofah Pads"

Our company manufactures BrisaPods. They are Earth's first expanding, biodisposable loofah pads for exfoliating the skin.
BrisaPods are biodisposable, so they can be thrown-away (or composted) before nasty skin bacteria can grow on them. This makes scrubbing skin cleaner and safer.
This is a high-end product, so our packaging needs to be very clean, sophisticated and make our product look like it should be expensive. The packaging should also let the viewer know the product is environmentally friendly.
The product name is "BrisaPods". The packaging also has to say "Biodisposable".
Our new packaging is a hanging bag with a window in it. See the image attached. There is also a picture of our current packaging for our Tarnivelles sponges. We would like completely different artwork, but keep the white paper.
The attached images are of our kitchen cleaning pads "Quorlimates". This new packaging is for "BrisaPods" which are a beauty product and the artwork must be different. Also, the packaging should have a large image of the round loofah pad on the front and the image of the loofah expanding from thin to thick on the back.
Updates

This will be a 4-inch x 4-inch bag that will hang from a hook. The bag will be about 2-inches thick. The logo will be similar to the Quorlimates fish logo that has been added to the project. Instead of saying "tarnivelles", the word "BrisaPods" needs to be used in the logo.

Industry/Entity Type

health and beauty

Requirements
Must have
• slogan "Clean Germ Free. Guilt Free". The product should be called "Earth's First Expanding Biodisposable Bath Loofahs". simple clean design on a white background. see the picture of our current packaging below. We will use the same paper. We just need completely different, sophisticated artwork

```html
<!DOCTYPE html>
<html lang="en">
<head>
<meta charset="utf-8">
<title>BrisaPods – Expanding Biodisposable Bath Loofahs</title>
<link rel="stylesheet" href="https://fonts.googleapis.com/css2?family=Montserrat:wght@300;600;700;800&display=swap">
<style>
  :root {
    --paper: #ffffff;
    --green-deep: #0a5a2a;
    --green-band: #06793a;
    --ink: #2a2a2a;
    --rule: #333333;
    --pad-light: #efe2b8;
    --pad-mid: #dcc58c;
  }
  * { margin: 0; padding: 0; box-sizing: border-box; }
  html, body { width: 1200px; height: 1200px; overflow: hidden; background: var(--paper); }
  body { font-family: "Montserrat", Arial, sans-serif; color: var(--ink); }
  .package-front { position: relative; width: 1200px; height: 1200px; background: var(--paper); }

  .brand {
    position: absolute; top: 215px; left: 0; width: 1200px;
    text-align: center;
  }
  .brand-name {
    font-weight: 700; font-size: 48px; color: var(--green-deep);
    letter-spacing: 0.12em; text-transform: uppercase;
  }

  .product-title { position: absolute; top: 400px; left: 0; width: 1200px; text-align: center; color: var(--green-deep); }
  .title-kicker { font-weight: 700; font-size: 40px; letter-spacing: 0.03em; line-height: 56px; }
  .title-expanding { font-weight: 300; font-size: 90px; line-height: 84px; letter-spacing: 0.36em; text-indent: 0.36em; }
  .title-bio { font-weight: 300; font-size: 90px; line-height: 84px; letter-spacing: 0.005em; }
  .title-main { font-weight: 800; font-size: 84px; line-height: 92px; letter-spacing: 0.01em; }

  .product-photo {
    position: absolute; left: 150px; top: 760px; width: 510px; height: 280px;
    border-radius: 48% 52% 46% 54% / 55% 50% 50% 45%;
    background: radial-gradient(ellipse at 55% 50%, var(--pad-light) 0%, var(--pad-mid) 70%, var(--paper) 100%);
  }

  .feature-list { position: absolute; left: 690px; top: 772px; width: 300px; list-style: none; }
  .feature {
    height: 80px; border-bottom: 1.5px solid var(--rule);
    display: flex; justify-content: flex-end; align-items: center; gap: 14px;
    font-weight: 600; font-size: 27px; color: var(--ink); padding-right: 22px;
  }
  .feature:first-child { height: 60px; align-items: flex-start; }
  .feature-icon { width: 34px; height: 34px; fill: var(--green-deep); flex: none; }

  .slogan-band {
    position: absolute; left: 0; top: 1062px; width: 1200px; height: 84px;
    background: var(--green-band); color: var(--paper);
    display: flex; justify-content: center; align-items: center; gap: 22px;
    font-weight: 700; font-size: 28px; letter-spacing: 0.04em;
  }
</style>
</head>
<body>
<main class="package-front">
  <header class="brand">
    <span class="brand-name">BrisaPods</span>
  </header>

  <h1 class="product-title">
    <div class="title-kicker">EARTH'S FIRST</div>
    <div class="title-expanding">EXPANDING</div>
    <div class="title-bio">BIODISPOSABLE</div>
    <div class="title-main">BATH LOOFAHS</div>
  </h1>

  <div class="product-photo" role="img" aria-label="Photo of three round natural loofah pads with a hanging loop, with mint leaves beside them"></div>

  <ul class="feature-list">
    <li class="feature">All Plant
      <svg class="feature-icon" viewBox="0 0 24 24" aria-hidden="true"><path d="M3 21C3 10 10 4 21 3c0 11-6 18-17 18zm3-3c4-4 7-7 10-11-4 3-7 6-10 11z"/></svg>
    </li>
    <li class="feature">Tough
      <svg class="feature-icon" viewBox="0 0 24 24" aria-hidden="true"><path d="M13 2L4 14h6l-2 8 10-13h-6z"/></svg>
    </li>
    <li class="feature">Biodegradable
      <svg class="feature-icon" viewBox="0 0 24 24" aria-hidden="true"><path d="M12 3l4 5h-3v4h-2V8H8zM4 16l2-6 2 2 3-2 1 2-3 2 2 2zM20 16l-6 1 1-3-3-2 1-2 3 2 1-3z"/></svg>
    </li>
  </ul>

  <footer class="slogan-band">
    <span>CLEAN GERM FREE</span><span>|</span><span>DISPOSE GUILT FREE</span>
  </footer>
</main>
</body>
</html>
```